KELD, Inc. new buisness cards - brand guide included

We need new business cards. SLEAK SIMPLE FINANCE. They must include a place for NAME, TITLE, CELL, OFFICE PHONE, EMAIL. they also must include our services across the bottom. AIR, OCEAN, FTL, LTL, EXPRESS. for reference this will be being handed to some of the most prestigious shipping companies in a america.

Target Market(s)

Finance and corporate

Contact Information for Business Card

We need new business cards. SLEAK SIMPLE FINANCE. They must include a place for NAME, TITLE, CELL, OFFICE PHONE, EMAIL. they also must include our services across the bottom. AIR, OCEAN, FTL, LTL, EXPRESS.

Requirements
Must have
• We need new business cards. SLEAK SIMPLE FINANCE. They must include a place for NAME, TITLE, CELL, OFFICE PHONE, EMAIL. they also must include our services across the bottom. AIR, OCEAN, FTL, LTL, EXPRESS.
Nice to have
• USE THE COLORS AND LOGO IN THE BRAND GUIDE :)

```html
<!DOCTYPE html>
<html lang="en">
<head>
<meta charset="utf-8">
<title>KELD, Inc. Business Card</title>
<link rel="stylesheet" href="https://fonts.googleapis.com/css2?family=Arimo:wght@400;700&display=swap">
<style>
  :root {
    --stage: #737373;
    --paper: #ffffff;
    --gold: #b9ab88;
    --gold-light: #d6cbb0;
    --gold-dark: #a29370;
    --ink: #1d1d1d;
    --onyx: #2c2c2c;
    --onyx-deep: #232323;
  }
  * { box-sizing: border-box; margin: 0; padding: 0; }
  html, body { width: 1200px; height: 802px; overflow: hidden; }
  body {
    background: var(--stage);
    font-family: "Arimo", Arial, sans-serif;
    position: relative;
  }
  .card {
    position: absolute;
    top: 246px;
    width: 540px;
    height: 309px;
    overflow: hidden;
  }
  .card-front { left: 50px; background: var(--paper); }
  .card-back {
    left: 610px;
    background: linear-gradient(135deg, var(--onyx) 0%, var(--onyx-deep) 100%);
  }
  .wordmark {
    position: absolute;
    left: 52px;
    top: 100px;
    font-size: 50px;
    font-weight: 400;
    letter-spacing: 6px;
    color: var(--gold);
  }
  .identity { position: absolute; left: 282px; top: 44px; }
  .person-name {
    font-size: 25px;
    font-weight: 700;
    color: var(--gold);
    letter-spacing: 0.5px;
  }
  .person-title {
    font-size: 13px;
    color: var(--gold);
    margin-top: 2px;
  }
  .contact-list {
    list-style: none;
    position: absolute;
    left: 282px;
    top: 108px;
  }
  .contact-item {
    display: flex;
    align-items: center;
    height: 23px;
    font-size: 14px;
    color: var(--ink);
  }
  .contact-icon { width: 16px; height: 16px; margin-right: 10px; flex: none; }
  .divider { position: absolute; left: 0; top: 0; }
  .services-label {
    position: absolute;
    left: 240px;
    top: 208px;
    width: 120px;
    height: 26px;
    border-radius: 13px;
    background: linear-gradient(180deg, var(--gold-light), var(--gold));
    color: var(--paper);
    font-size: 13px;
    font-weight: 700;
    letter-spacing: 1px;
    display: flex;
    align-items: center;
    justify-content: center;
  }
  .services-list {
    position: absolute;
    left: 182px;
    top: 279px;
    font-size: 15px;
    font-weight: 700;
    color: var(--paper);
    letter-spacing: 1px;
    white-space: nowrap;
  }
  .back-pattern { position: absolute; inset: 0; }
  .back-wordmark {
    position: absolute;
    left: 50%;
    top: 50%;
    transform: translate(-50%, -50%);
    font-size: 30px;
    letter-spacing: 5px;
    color: var(--paper);
  }
</style>
</head>
<body>
  <section class="card card-front" aria-label="Business card front">
    <div class="wordmark">KELD</div>

    <div class="identity">
      <h1 class="person-name">SELIN ARKOMA</h1>
      <p class="person-title">Founder &amp; CEO</p>
    </div>

    <ul class="contact-list">
      <li class="contact-item">
        <svg class="contact-icon" viewBox="0 0 16 16"><circle cx="8" cy="8" r="8" fill="var(--gold)"/><path d="M5 4.5l1.5-.5 1 2-1 .8a5 5 0 0 0 2.7 2.7l.8-1 2 1-.5 1.5c-3.5 0-6.5-3-6.5-6.5z" fill="#fff"/></svg>
        012-555-018-274
      </li>
      <li class="contact-item">
        <svg class="contact-icon" viewBox="0 0 16 16"><circle cx="8" cy="8" r="8" fill="var(--gold)"/><rect x="4.5" y="6.5" width="7" height="5" rx="1" fill="#fff"/><path d="M4 6c1-1.5 7-1.5 8 0" stroke="#fff" stroke-width="1.2" fill="none"/></svg>
        044-555-019-362
      </li>
      <li class="contact-item">
        <svg class="contact-icon" viewBox="0 0 16 16"><circle cx="8" cy="8" r="8" fill="var(--gold)"/><path d="M4 8.5l8-4-2.5 8-1.8-2.6z" fill="#fff"/></svg>
        info@keldinc.com
      </li>
      <li class="contact-item">
        <svg class="contact-icon" viewBox="0 0 16 16"><circle cx="8" cy="8" r="8" fill="var(--gold)"/><g stroke="#fff" stroke-width="1" fill="none"><circle cx="8" cy="8" r="4"/><ellipse cx="8" cy="8" rx="1.8" ry="4"/><path d="M4 8h8"/></g></svg>
        www.keldinc.com
      </li>
    </ul>

    <svg class="divider" width="540" height="309" viewBox="0 0 540 309" aria-hidden="true">
      <defs>
        <linearGradient id="band-gold" x1="0" y1="0" x2="1" y2="0">
          <stop offset="0" stop-color="var(--gold-dark)"/>
          <stop offset="0.5" stop-color="var(--gold-light)"/>
          <stop offset="1" stop-color="var(--gold-dark)"/>
        </linearGradient>
      </defs>
      <line x1="30" y1="218" x2="510" y2="218" stroke="var(--gold)" stroke-width="1"/>
      <line x1="30" y1="224" x2="510" y2="224" stroke="var(--gold)" stroke-width="1"/>
      <polygon points="0,300 150,300 172,268 515,268 540,260 540,309 0,309" fill="url(#band-gold)"/>
    </svg>

    <div class="services-label">SERVICES</div>
    <p class="services-list">AIR &bull; OCEAN &bull; FTL &bull; LTL &bull; EXPRESS</p>
  </section>

  <section class="card card-back" aria-label="Business card back">
    <div class="back-pattern" role="img" aria-label="Embossed repeating brand pattern across dark card stock"></div>
    <div class="back-wordmark">KELD</div>
  </section>
</body>
</html>
```